Torvela Lighting needs a new website (only informative)

Torvela Lighting (Pty) Ltd imports and distributes LED lighting products to South Africa. Our existing website (www.torvela.co.za) is designed and implemented on a shopping cart template: Pix-Basket.

The website needs to be redesigned. It should no longer be based on a shopping cart template, but purely informative and allow some PDF downloads. It should scale well and allow quick & easy changes by the website owner: Including adding, changing and removing products. Other information pages should also be easy to manage.

No need to design a logo. A logo and user requirement specification is uploaded with more details.

Target Market(s)

Retailers, interior designers, architects, contractors, electricians, franchises etc. with a need for energy efficient LED lighting.

Industry/Entity Type

Shopping

Font styles to use
Sans Serif

Colors
0355a3
0892cd
86cae6
86cfc6

Requirements
Must have
• Existing logo to be used.
All pages informative & PDF download capability.
User friendly management
SEO capability

```html
<!DOCTYPE html>
<html lang="en">
<head>
<meta charset="utf-8">
<title>Torvela Lighting – LED Lights</title>
<link href="https://fonts.googleapis.com/css2?family=Lato:wght@400;700&family=Oswald:wght@400;500&display=swap" rel="stylesheet">
<style>
:root{
  --navy:#0355a3;
  --blue:#0892cd;
  --sky:#86cae6;
  --teal:#86cfc6;
  --light:#b9dff0;
  --ink:#4a4a4a;
  --muted:#7d7d7d;
  --line:#dcdcdc;
  --dark:#2f3338;
  --darker:#25282c;
  --white:#ffffff;
}
*{box-sizing:border-box;margin:0;padding:0}
html,body{width:1200px;height:3303px;overflow:hidden}
body{position:relative;background:var(--white);font-family:'Lato',sans-serif;color:var(--ink);font-size:14px;line-height:1.5}
.section{position:absolute;left:0;width:1200px}
.wrap{position:absolute;left:155px;width:890px}
h2,h3,h4{font-family:'Oswald',sans-serif;font-weight:400}
a{color:inherit;text-decoration:none}

/* header */
.header{top:0;height:198px;background:var(--white);border-bottom:4px solid var(--blue)}
.topbar-social{position:absolute;right:140px;top:6px;display:flex;gap:10px}
.topbar-social span{width:14px;height:14px;background:#9aa3ab;border-radius:2px}
.logo{position:absolute;left:155px;top:80px;display:flex;align-items:center;gap:10px}
.logo-mark{width:22px;height:22px;border-radius:50%;background:var(--navy)}
.logo-name{font-family:'Lato',sans-serif;font-weight:700;font-size:34px;color:var(--navy);letter-spacing:1px}
.logo-sub{position:absolute;left:187px;top:114px;font-size:11px;font-weight:700;color:var(--navy);letter-spacing:2px}
.nav{position:absolute;left:470px;top:60px;display:flex}
.nav a{display:block;width:116px;text-align:center;font-family:'Oswald',sans-serif;font-size:13px;color:#8a8a8a;text-transform:uppercase;letter-spacing:1px;line-height:1.3}
.nav-marker{position:absolute;left:470px;top:132px;width:116px;height:1px;background:var(--line)}

/* hero */
.hero{top:198px;height:440px;background:linear-gradient(180deg,#0b1220 0%,#1d2a3a 40%,#4a2e1a 60%,#1a1410 100%)}
.hero-streaks{position:absolute;inset:0;background:linear-gradient(160deg,transparent 45%,rgba(255,170,90,.35) 52%,rgba(255,230,200,.45) 56%,rgba(230,60,40,.3) 60%,transparent 68%)}
.hero-arrow{position:absolute;top:200px;width:36px;height:40px;background:rgba(255,255,255,.8);border-radius:3px}
.hero-arrow.left{left:14px}.hero-arrow.right{right:14px}
.hero-dots{position:absolute;left:552px;top:394px;width:96px;height:22px;background:rgba(255,255,255,.85);border-radius:11px;display:flex;align-items:center;justify-content:center;gap:8px}
.hero-dots i{width:9px;height:9px;border-radius:50%;background:#999}
.hero-dots i.on{background:var(--navy)}

/* about */
.about{top:638px;height:682px;background:linear-gradient(180deg,#0a84c8,var(--blue) 60%,#1296cf)}
.about-intro{left:155px;top:60px;width:265px;color:var(--white)}
.about-intro h2{font-size:28px;margin-bottom:16px}
.about-intro p{font-size:13px;line-height:1.55}
.about-features{left:482px;top:62px;width:563px;display:grid;grid-template-columns:1fr 1fr;column-gap:40px;row-gap:48px}
.feature{color:var(--white)}
.feature svg{display:block;margin-bottom:10px}
.feature h3{font-size:18px;margin-bottom:4px}
.feature p{font-size:13px;line-height:1.5;margin-bottom:12px}
.btn-more{display:inline-block;font-size:11px;padding:3px 14px;border-radius:12px;background:var(--navy);color:var(--white)}

/* belief banner */
.banner{top:1361px;left:155px;width:890px;height:174px;border:1px solid var(--line);box-shadow:0 2px 4px rgba(0,0,0,.08);background:linear-gradient(180deg,#fff,#f3f3f3)}
.banner p{position:absolute;left:14px;top:58px;font-family:'Oswald',sans-serif;font-size:19px;color:#666;line-height:1.45}
.banner-photo{position:absolute;right:20px;top:16px;width:340px;height:142px;background:radial-gradient(ellipse at center,#eef3f6 0%,#d7dde2 60%,#fafafa 100%)}

/* benefits */
.benefits{top:1590px;display:grid;grid-template-columns:repeat(4,1fr);column-gap:24px}
.benefit h4{font-size:15px;color:#333;display:flex;align-items:center;gap:8px;margin-bottom:4px}
.benefit p{font-size:12px;color:var(--muted);padding-left:40px;line-height:1.45}
.benefit .more{display:block;font-size:11px;color:var(--blue);margin-top:10px}

/* section heading */
.sec-head{font-family:'Oswald',sans-serif;font-size:15px;color:#555;text-transform:uppercase;border-bottom:1px solid var(--line);padding-bottom:4px}
.pager{position:absolute;right:0;top:2px;display:flex;gap:2px}
.pager span{width:18px;height:16px;background:#c8d3d8}
.pager span.on{background:var(--teal)}

/* products */
.products-head{top:1826px}
.products{top:1878px;height:427px;display:grid;grid-template-columns:repeat(5,1fr)}
.product{background:var(--sky);display:flex;flex-direction:column}
.product:nth-child(odd){background:var(--blue)}
.product:nth-child(3){background:var(--light)}
.product-code{height:44px;line-height:44px;text-align:center;font-family:'Oswald',sans-serif;font-size:16px;color:var(--white);background:rgba(255,255,255,.18)}
.product:nth-child(3) .product-code{color:var(--navy)}
.product-img{height:128px}
.product h4{text-align:center;font-size:13px;color:var(--white);padding:8px 0;margin:0 10px;border-bottom:1px solid rgba(255,255,255,.6)}
.product:nth-child(3) h4{color:#333;border-color:#8ab}
.product p{font-size:12px;color:var(--white);padding:10px;line-height:1.45}
.product:nth-child(3) p{color:#333}

/* clients */
.clients-head{top:2423px}
.clients{top:2464px;height:107px;display:grid;grid-template-columns:repeat(5,1fr);align-items:center;border-bottom:1px solid var(--line)}
.client{display:flex;align-items:center;justify-content:center;gap:8px;font-weight:700;font-size:17px;color:#39424a}
.client i{width:14px;height:14px;background:var(--navy);border-radius:50%}

/* articles */
.articles{top:2668px;height:206px;background:var(--dark);border-top:6px solid #f0f0f0}
.articles-tab{position:absolute;left:155px;top:-6px;width:108px;height:22px;background:var(--blue);color:var(--white);font-family:'Oswald',sans-serif;font-size:13px;text-align:center;line-height:22px;text-transform:uppercase}
.article{position:absolute;top:48px;display:flex;gap:12px}
.article-photo{width:104px;height:78px}
.article time{display:block;font-size:11px;color:var(--blue)}
.article h4{font-size:15px;color:var(--blue);line-height:1.3}
.article .by{font-size:12px;color:var(--white);font-weight:700;margin-top:8px}
.articles-rule{position:absolute;left:0;right:0;bottom:0;height:4px;background:var(--blue)}

/* footer */
.footer{top:2874px;height:385px;background:var(--dark);color:#9aa0a6}
.footer h4{position:absolute;top:42px;font-size:15px;color:var(--white);text-transform:uppercase}
.col{position:absolute;top:90px;font-size:12px;line-height:1.5}
.tweet-box{width:206px;height:52px;background:#3e4349;border-radius:3px;padding:6px 10px;color:var(--white);font-size:12px}
.tweet-box .tw-title{text-align:right;font-size:11px}
.social-row{display:flex;gap:14px;margin-top:20px}
.social-row i{width:14px;height:14px;background:#9aa0a6;border-radius:50%}
.gallery{width:150px;height:228px;background:linear-gradient(135deg,#6b7f99,#394552 40%,#8a5c3f 70%,#2c3440)}
.contact dt{color:var(--white);display:flex;align-items:center;gap:6px;margin-top:6px}
.contact dd{padding-left:18px}
.footer-legal a{color:var(--teal)}

.bottombar{top:3259px;height:44px;background:var(--darker);font-size:12px;color:#9aa0a6}
.bottombar nav{position:absolute;left:64px;top:13px}
.to-top{position:absolute;right:52px;top:-20px;width:30px;height:30px;background:#5a6068;border-radius:3px}
</style>
</head>
<body>

<header class="section header">
  <div class="topbar-social"><span></span><span></span><span></span><span></span><span></span></div>
  <div class="logo"><span class="logo-mark"></span><span class="logo-name">torvela</span></div>
  <div class="logo-sub">LED LIGHTS</div>
  <nav class="nav">
    <a href="#">Home</a>
    <a href="#">Lighting<br>Fundamentals</a>
    <a href="#">Products</a>
    <a href="#">Contact</a>
    <a href="#">References</a>
  </nav>
  <div class="nav-marker"></div>
</header>

<section class="section hero" role="img" aria-label="Night city highway with long-exposure light trails">
  <div class="hero-streaks"></div>
  <div class="hero-arrow left"></div>
  <div class="hero-arrow right"></div>
  <div class="hero-dots"><i class="on"></i><i></i><i></i></div>
</section>

<section class="section about">
  <div class="wrap about-intro">
    <h2>About Us</h2>
    <p>Founded in 2009, Torvela is directed and operated by qualified staff in a manner to minimise cost to deliver exceptional value to our customers. We started off with most of the company operations automated which allowed time to be spent on technology, research and product development.<br>Significant growth and demand for our products enabled us to focus on the wholesale and distribution markets. From our warehouse situated in Halfway – Midrand Business Park, we serve our customers nationally and to neighbouring countries. Expansion into Africa is considered for the medium term.</p>
  </div>
  <div class="wrap about-features">
    <div class="feature">
      <svg width="34" height="34" viewBox="0 0 34 34"><circle cx="17" cy="14" r="8" fill="none" stroke="#fff" stroke-width="2.5"/><rect x="13" y="23" width="8" height="6" fill="#fff"/></svg>
      <h3>Product</h3>
      <p>Our current product suite consist purely of LED (Light Emitting Diode) bulbs. Most LED bulbs on the South African market today are known for either very poor light..</p>
      <a class="btn-more" href="#">Learn more</a>
    </div>
    <div class="feature">
      <svg width="34" height="34" viewBox="0 0 34 34"><circle cx="17" cy="17" r="15" fill="#fff"/><text x="17" y="24" text-anchor="middle" font-size="20" font-family="Lato,sans-serif" font-weight="700" fill="#0892cd">?</text></svg>
      <h3>Why Torvela</h3>
      <p>All products are thoroughly evaluated, tested and benchmarked to ensure the best that LED technology has to offer. By getting involved in the design process we ensure compliance with..</p>
      <a class="btn-more" href="#">Learn more</a>
    </div>
    <div class="feature">
      <svg width="34" height="34" viewBox="0 0 34 34"><circle cx="17" cy="17" r="8" fill="none" stroke="#fff" stroke-width="2.5"/><path d="M4 17h6M24 17h6M17 4v6M17 24v6" stroke="#fff" stroke-width="2.5"/></svg>
      <h3>Vision</h3>
      <p>To ensure quality of life today and for generations to come through efficiency and energy saving.</p>
      <a class="btn-more" href="#">Learn more</a>
    </div>
    <div class="feature">
      <svg width="34" height="34" viewBox="0 0 34 34"><path d="M8 26L26 8" stroke="#fff" stroke-width="3"/><path d="M20 6h8v8" fill="none" stroke="#fff" stroke-width="2.5"/></svg>
      <h3>Mission</h3>
      <p>To research, source and promote leading edge technology at the best possible price.</p>
      <a class="btn-more" href="#">Learn more</a>
    </div>
  </div>
</section>

<section class="section banner">
  <p>We believe in a cleaner tomorrow. Join us in conserving power.<br>We enable you through efficient &amp; affordable LED products.</p>
  <div class="banner-photo" role="img" aria-label="Group of white LED bulbs and spotlights"></div>
</section>

<section class="wrap benefits" style="position:absolute">
  <div class="benefit">
    <h4><svg width="30" height="30" viewBox="0 0 30 30"><rect x="4" y="5" width="22" height="18" fill="none" stroke="#2e9a6a" stroke-width="2"/><path d="M10 14l4 4 7-8" fill="none" stroke="#2e9a6a" stroke-width="2"/></svg>Certification</h4>
    <p>Our products are CE and RoHS certified, and comply with South..</p>
    <a class="more" href="#">Learn more ›</a>
  </div>
  <div class="benefit">
    <h4><svg width="30" height="30" viewBox="0 0 30 30"><rect x="5" y="5" width="18" height="20" fill="none" stroke="#0892cd" stroke-width="2"/><path d="M12 20l12-12" stroke="#0892cd" stroke-width="2"/></svg>Reviews</h4>
    <p>The first LED product that produce enough light. Reasonable..</p>
    <a class="more" href="#">Learn more ›</a>
  </div>
  <div class="benefit">
    <h4><svg width="30" height="30" viewBox="0 0 30 30"><path d="M15 3l3.5 8 8.5.8-6.4 5.6 2 8.4L15 21.5 7.4 25.8l2-8.4L3 11.8l8.5-.8z" fill="none" stroke="#f0a020" stroke-width="2"/></svg>Bestsellers</h4>
    <p>Browse through our bestselling products and decide for yourself..</p>
    <a class="more" href="#">Learn more ›</a>
  </div>
  <div class="benefit">
    <h4><svg width="30" height="30" viewBox="0 0 30 30"><rect x="4" y="8" width="22" height="15" fill="none" stroke="#e0513a" stroke-width="2"/><path d="M4 8l11 8 11-8" fill="none" stroke="#e0513a" stroke-width="2"/></svg>Newsletter</h4>
    <p>Subscribe to our newsletter to stay updated with what's new.</p>
    <a class="more" href="#">Learn more ›</a>
  </div>
</section>

<div class="wrap products-head" style="position:absolute"><h3 class="sec-head">Latest Products</h3><div class="pager"><span></span><span class="on"></span></div></div>
<section class="wrap products" style="position:absolute">
  <article class="product"><div class="product-code">TV-PN600</div><div class="product-img" role="img" aria-label="Square LED panel" style="background:linear-gradient(160deg,#e8eef3,#9fb0c0)"></div><h4>PANELS</h4><p>Torvela panels are only 10mm thick with an array of SMDs behind frosted glass. Driven with an external power supply which is provided with each unit.</p></article>
  <article class="product"><div class="product-code">TV-DL45 4.5W</div><div class="product-img" role="img" aria-label="LED downlight spotlight" style="background:linear-gradient(160deg,#fff3c0,#f3c23a)"></div><h4>DOWNLIGHTS</h4><p>Ultra efficient, high intensity LED downlight. The 4x COB LEDs deliver 340Lm. The beam width of stock items is lower at 30°, but on request up to 90° can also be ordered.</p></article>
  <article class="product"><div class="product-code">TV-BL32</div><div class="product-img" role="img" aria-label="Frosted LED bulb" style="background:radial-gradient(circle,#ffffff 30%,#dde3e8 100%)"></div><h4>BULBS</h4><p>Ultra efficient, high intensity LED lamp consisting of 32x 3528 SMDs. Frosted glass is used to diffuse light evenly.</p></article>
  <article class="product"><div class="product-code">TV-DL60</div><div class="product-img" role="img" aria-label="SMD LED downlight" style="background:linear-gradient(160deg,#fde7c4,#e9a24a)"></div><h4>DOWNLIGHTS</h4><p>Ultra efficient, high intensity LED downlight. The 4x COB LEDs deliver 340Lm. The beam width of stock items is lower at 30°, but on request up to 90° can also be ordered.</p></article>
  <article class="product"><div class="product-code">100W</div><div class="product-img" role="img" aria-label="Industrial LED highbay lamp" style="background:linear-gradient(180deg,#f2f2f2,#8f9aa3)"></div><h4>HIGHBAYS</h4><p>High power single LED chip lamp in a robust heavy body. Both deep and shallow diffusers (cones) are available to control the beam width.</p></article>
</section>

<div class="wrap clients-head" style="position:absolute"><h3 class="sec-head">Our Clients</h3><div class="pager"><span></span><span class="on"></span></div></div>
<section class="wrap clients" style="position:absolute">
  <div class="client"><i></i>Veldkrag</div>
  <div class="client"><i></i>Karoo Grid</div>
  <div class="client"><i></i>Meridane</div>
  <div class="client"><i></i>Voltrex</div>
  <div class="client"><i></i>Kestra</div>
</section>

<section class="section articles">
  <div class="articles-tab">Articles</div>
  <div class="article" style="left:155px">
    <div class="article-photo" role="img" aria-label="House lit with festive LED lights at night" style="background:linear-gradient(160deg,#1c2a4a,#c98a3a)"></div>
    <div><time>08 Dec, 2012</time><h4>Switch to LED Christmas Lights</h4><p class="by">by Miriam Hale</p></div>
  </div>
  <div class="article" style="left:612px">
    <div class="article-photo" role="img" aria-label="Wind turbines under a blue sky" style="background:linear-gradient(180deg,#4a8fd0,#d6e6f2)"></div>
    <div><time>30 Sep, 2012</time><h4>The Future of Clean Energy is Arriving</h4><p class="by">by Daniel Ferreira</p></div>
  </div>
  <div class="articles-rule"></div>
</section>

<footer class="section footer">
  <h4 style="left:155px">Directors</h4>
  <div class="col" style="left:155px;width:200px">
    <p>P J Venter<br>(M Eng – Electronic Engineering)<br>A M Naude (B. Com)<br>Registration number:<br>2010/123456/07<br>VAT number: 4120987654</p>
    <p style="margin-top:52px">© 2013. All Rights Reserved.</p>
    <p class="footer-legal"><a href="#">Terms of Service</a> | <a href="#">Privacy Policy</a></p>
  </div>
  <h4 style="left:384px">Stay Connected</h4>
  <div class="col" style="left:384px">
    <div class="tweet-box"><div class="tw-title">Latest tweet</div>@torvela</div>
    <div class="social-row"><i></i><i></i><i></i><i></i></div>
    <div class="social-row" style="margin-top:14px"><i></i></div>
  </div>
  <h4 style="left:612px">Gallery</h4>
  <div class="col" style="left:628px"><div class="gallery" role="img" aria-label="Grid of LED installation photos"></div></div>
  <h4 style="left:838px">Contact Information</h4>
  <dl class="col contact" style="left:838px;width:210px">
    <dt><svg width="12" height="14" viewBox="0 0 12 14"><path d="M6 0a5 5 0 0 1 5 5c0 4-5 9-5 9S1 9 1 5a5 5 0 0 1 5-5z" fill="#9aa0a6"/></svg>Address:</dt>
    <dd>• 48 Falcon Road, Midrand Business Park, Halfway, 1685</dd>
    <dd>• Unit 7 Cnr Kloof &amp; Mill Streets, Parow, 7500</dd>
    <dt><svg width="12" height="12" viewBox="0 0 12 12"><path d="M2 1l3 3-1.5 1.5a7 7 0 0 0 3 3L8 7l3 3-2 2C4 12 0 8 0 3z" fill="#9aa0a6"/></svg>Phone:</dt>
    <dd>+27 12 555 0147<br>+27 21 555 0192</dd>
    <dt><svg width="12" height="10" viewBox="0 0 12 10"><rect x="0" y="0" width="12" height="10" fill="#9aa0a6"/><path d="M0 0l6 5 6-5" stroke="#2f3338" fill="none"/></svg>Email:</dt>
    <dd>sales@torvela.co.za<br>info@torvela.co.za<br>support@torvela.co.za</dd>
  </dl>
</footer>

<div class="section bottombar">
  <div class="to-top"></div>
  <nav>Home &nbsp;|&nbsp; Lighting Fundamentals &nbsp;|&nbsp; Products &nbsp;|&nbsp; Contact &nbsp;|&nbsp; References</nav>
</div>

</body>
</html>
```